Flyer Design Project

Painting and Maintenance
This is what I have as idea as Job description
Refresh, renew & revive your home. from painting to carpentry. Do you guys have any epic unique slogan?
As what we do Residential - Commercial Interior - ExteriorTrim & Molding installationWainscoting - Wallpaper removalCabinet refinishing Woodwork EnamelingDeck & Fence Cleaning & SealingPressure washConcrete & Paver Washing
I would like to have a note that says-Prompt professional service-Free estimates-Insured -"visit us on ChatHive"
I would like new ideas from you guys as well!
Carpentry

```html
<!DOCTYPE html>
<html lang="en">
<head>
<meta charset="utf-8">
<title>Hartwell Painting &amp; Maintenance – Flyer</title>
<link rel="stylesheet" href="https://fonts.googleapis.com/css2?family=Archivo+Black&family=Lato:wght@400;700;900&family=Oswald:wght@700&family=Roboto:ital,wght@1,700&display=swap">
<style>
  :root{
    --red:#d40d0d;
    --red-deep:#b81212;
    --charcoal:#424245;
    --charcoal-dark:#333336;
    --white:#ffffff;
    --backdrop:#8d8d8f;
    --logo-ink:#3a3a3c;
  }
  *{margin:0;padding:0;box-sizing:border-box}
  html,body{width:1200px;height:1200px;overflow:hidden;background:var(--backdrop)}
  .flyer{
    position:absolute;left:205px;top:0;width:836px;height:1270px;
    transform:scale(0.945);transform-origin:top left;
    background:var(--white);overflow:hidden;
  }
  .header{
    position:absolute;left:0;top:0;width:836px;height:242px;
    background:linear-gradient(180deg,var(--red-deep),var(--red));
    text-align:center;color:var(--white);
    font-family:"Archivo Black",sans-serif;
  }
  .header .line-1{position:absolute;top:34px;left:0;right:0;font-size:46px;letter-spacing:1px}
  .header .line-2{position:absolute;top:89px;left:0;right:0;font-size:46px;letter-spacing:1px}
  .header .tagline{position:absolute;top:145px;left:0;right:0;font-size:40px;letter-spacing:.5px}
  .rule{position:absolute;left:230px;right:0;height:4px;background:var(--charcoal)}
  .rule.top{top:240px}.rule.bottom{top:248px}
  .hero{
    position:absolute;left:0;top:254px;width:836px;height:446px;
    background:linear-gradient(180deg,#e6ebf3 0%,#c7cfdc 35%,#9a9ca6 60%,#b99676 85%,#7d6652 100%);
  }
  .brand{
    position:absolute;left:0;top:200px;width:340px;height:170px;
    background:linear-gradient(90deg,rgba(255,255,255,.95),rgba(255,255,255,.8) 70%,rgba(255,255,255,0));
    padding:60px 0 0 26px;
  }
  .brand-name{
    font-family:"Lato",sans-serif;font-weight:900;color:var(--logo-ink);
    font-size:34px;line-height:1.05;
  }
  .thumbs{position:absolute;left:14px;top:700px;width:812px;height:180px;display:flex;gap:10px}
  .thumb{flex:1;border:4px solid var(--white);box-shadow:0 0 0 1px #ccc}
  .thumb.exterior{background:linear-gradient(180deg,#b9c8d6,#8a2f2b 45%,#6e2926 80%,#3f5b2e)}
  .thumb.kitchen{background:linear-gradient(180deg,#f1f1ef,#dcd7cf 55%,#4b4b4d)}
  .thumb.patio{background:linear-gradient(135deg,#6c7278,#8d939a 50%,#55605a)}
  .services{position:absolute;left:0;top:882px;width:836px;height:220px;background:var(--charcoal)}
  .services-title{
    position:absolute;left:297px;top:6px;width:242px;height:46px;border-radius:23px;
    background:var(--red);border:2px solid var(--white);
    font-family:"Oswald",sans-serif;font-weight:700;font-size:29px;color:var(--white);
    text-align:center;line-height:40px;
  }
  .service-col{position:absolute;top:66px;list-style:none;font-family:"Lato",sans-serif;font-size:18.5px;color:var(--white)}
  .service-col li{position:relative;padding-left:28px;margin-bottom:12px;line-height:23px}
  .service-col li svg{position:absolute;left:0;top:2px;width:18px;height:16px}
  .col-1{left:26px;width:250px}
  .col-2{left:308px;width:240px;border-left:2px solid var(--white);padding-left:16px;height:122px}
  .col-3{left:548px;width:260px;border-left:2px solid var(--white);padding-left:26px;height:122px}
  .col-2,.col-3{top:66px}
  .promises{position:absolute;left:0;top:1102px;width:836px;height:94px;background:var(--white)}
  .promise{position:absolute;top:12px;font-family:"Roboto",sans-serif;font-style:italic;font-weight:700;font-size:26px;line-height:36px;color:var(--red)}
  .promise .dot{position:absolute;left:-62px;top:10px;width:46px;height:46px;border-radius:50%;background:var(--charcoal)}
  .promise.service{left:80px}
  .promise.estimates{left:521px}
  .footer{
    position:absolute;left:120px;top:1195px;width:716px;height:60px;background:var(--red);
    clip-path:polygon(14px 0,100% 0,100% 100%,0 100%);
  }
  .brush{position:absolute;left:20px;top:1188px;width:104px;height:70px;background:linear-gradient(135deg,#5a5a5d,#8c1010);border-radius:30px 6px 30px 6px;transform:rotate(28deg)}
  .social{
    position:absolute;left:154px;top:1212px;display:flex;align-items:center;gap:18px;
    font-family:"Lato",sans-serif;font-size:21px;color:var(--white);
  }
  .social .square{width:26px;height:26px;background:var(--white)}
</style>
</head>
<body>
<main class="flyer">
  <header class="header">
    <div class="line-1">REFRESH, RENEW &amp; REVIVE</div>
    <div class="line-2">YOUR HOME</div>
    <div class="tagline">from painting to carpentry</div>
  </header>
  <div class="rule top"></div>
  <div class="rule bottom"></div>

  <div class="hero" role="img" aria-label="Photo of a large two-storey grey shingle house with lit windows and a paved driveway at dusk"></div>

  <div class="brand">
    <div class="brand-name">Hartwell Painting<br>&amp; Maintenance LLC</div>
  </div>

  <div class="thumbs">
    <div class="thumb exterior" role="img" aria-label="Photo of a red clapboard house being painted with ladders against it"></div>
    <div class="thumb kitchen" role="img" aria-label="Photo of a refinished white kitchen with tiled backsplash and range"></div>
    <div class="thumb patio" role="img" aria-label="Photo of stone pavers being sealed with a roller"></div>
  </div>

  <section class="services">
    <h2 class="services-title">WHAT WE DO</h2>
    <ul class="service-col col-1">
      <li><svg viewBox="0 0 18 16"><path d="M1 1h12v2H3v10h10V9h2v6H1z" fill="#fff"/><path d="M4 7l3 3 9-9" stroke="#fff" stroke-width="2.4" fill="none"/></svg>Residential</li>
      <li><svg viewBox="0 0 18 16"><path d="M1 1h12v2H3v10h10V9h2v6H1z" fill="#fff"/><path d="M4 7l3 3 9-9" stroke="#fff" stroke-width="2.4" fill="none"/></svg>Commercial Interior</li>
      <li><svg viewBox="0 0 18 16"><path d="M1 1h12v2H3v10h10V9h2v6H1z" fill="#fff"/><path d="M4 7l3 3 9-9" stroke="#fff" stroke-width="2.4" fill="none"/></svg>ExteriorTrim &amp; Molding installation</li>
    </ul>
    <ul class="service-col col-2">
      <li><svg viewBox="0 0 18 16"><path d="M1 1h12v2H3v10h10V9h2v6H1z" fill="#fff"/><path d="M4 7l3 3 9-9" stroke="#fff" stroke-width="2.4" fill="none"/></svg>Wainscoting</li>
      <li><svg viewBox="0 0 18 16"><path d="M1 1h12v2H3v10h10V9h2v6H1z" fill="#fff"/><path d="M4 7l3 3 9-9" stroke="#fff" stroke-width="2.4" fill="none"/></svg>Wallpaper removal</li>
      <li><svg viewBox="0 0 18 16"><path d="M1 1h12v2H3v10h10V9h2v6H1z" fill="#fff"/><path d="M4 7l3 3 9-9" stroke="#fff" stroke-width="2.4" fill="none"/></svg>Cabinet refinishing</li>
      <li><svg viewBox="0 0 18 16"><path d="M1 1h12v2H3v10h10V9h2v6H1z" fill="#fff"/><path d="M4 7l3 3 9-9" stroke="#fff" stroke-width="2.4" fill="none"/></svg>Woodwork Enameling</li>
    </ul>
    <ul class="service-col col-3">
      <li><svg viewBox="0 0 18 16"><path d="M1 1h12v2H3v10h10V9h2v6H1z" fill="#fff"/><path d="M4 7l3 3 9-9" stroke="#fff" stroke-width="2.4" fill="none"/></svg>Deck &amp; Fence Cleaning</li>
      <li><svg viewBox="0 0 18 16"><path d="M1 1h12v2H3v10h10V9h2v6H1z" fill="#fff"/><path d="M4 7l3 3 9-9" stroke="#fff" stroke-width="2.4" fill="none"/></svg>Sealing Pressure wash</li>
      <li><svg viewBox="0 0 18 16"><path d="M1 1h12v2H3v10h10V9h2v6H1z" fill="#fff"/><path d="M4 7l3 3 9-9" stroke="#fff" stroke-width="2.4" fill="none"/></svg>Concrete &amp; Paver Washing</li>
    </ul>
  </section>

  <section class="promises">
    <p class="promise service"><span class="dot"></span>PROMPT PROFESSIONAL<br>SERVICE</p>
    <p class="promise estimates"><span class="dot"></span>FREE ESTIMATES<br>INSURED</p>
  </section>

  <div class="footer"></div>
  <div class="brush" role="img" aria-label="Illustration of a paintbrush with red paint"></div>
  <p class="social"><span class="square"></span>Visit us on ChatHive : /Hartwell-Painting-Maintenance-LLC</p>
</main>
</body>
</html>
```